New Look for our Work Trucks

Help us with a new look for our work trucks. Our company name is Marlowe Carpet Care, Inc. but cleaning of carpet is NOT all what we clean. Been in business since 1974 so we do NOT want to remove the word "Carpet" but we do NOT want it to stand out very much. For inside homes and business we clean carpet, upholstery, hard surface floors such as LVT, Tile & Grout, VCT and concrete. We also remove water from flooding. We are now also providing to the outside of homes and businesses Soft Washing & Power Washing. Soft Washing cleans Siding, Roofs, Gutters, Windows and Fencing and Power Washing cleans side walks and concrete drive ways. We will soon be adding Duct Cleaning Services as well. Our current web site is www.marlowecarpetcare-example.com. We are leaning towards a combination of pink and blue for our colors. Your hard work is greatly appreciated.

Target Market(s)

Residential & Commercial

Industry/Entity Type

Cleaning

Requirements
Must have
• We do NOT want to remove the word "carpet" out of our name but we do NOT want it to stand out very much.
Nice to have
• With less and less carpet being installed, we feel it is important to make sure the customer knows that we take care of both the inside & outside of their home or business. We do not want to be know as just carpet cleaners. Leaning towards pink & blue as colors
Should not have
• a focus on the word carpet.

```html
<!DOCTYPE html>
<html lang="en">
<head>
<meta charset="utf-8">
<title>Marlowe Carpet Care – Work Truck Wrap</title>
<link rel="stylesheet" href="https://fonts.googleapis.com/css2?family=Oswald:wght@400;500;600&display=swap">
<style>
  :root {
    --pink: #ec3f9c;
    --magenta: #b62fbf;
    --purple: #7b2fd2;
    --blue: #2c3fd8;
    --deep-blue: #1d2db4;
    --ribbon-red: #e2306b;
    --ink: #14141c;
    --name-grey: #e9e9f0;
    --white: #ffffff;
    --page: #ffffff;
    --panel-edge: #d7d7df;
  }
  * { box-sizing: border-box; margin: 0; padding: 0; }
  html, body { width: 1200px; height: 1008px; overflow: hidden; background: var(--page); }
  body { position: relative; font-family: "Oswald", "Arial Narrow", sans-serif; }

  .wrap-side {
    position: absolute; left: 50px; width: 1100px; height: 430px;
    border-radius: 26px; overflow: hidden; border: 1px solid var(--panel-edge);
    background: var(--white);
  }
  .wrap-side--driver { top: 44px; }
  .wrap-side--passenger { top: 534px; }
  .wrap-side svg.art { position: absolute; inset: 0; width: 100%; height: 100%; }

  .glow {
    position: absolute; width: 260px; height: 260px; border-radius: 50%;
    background: radial-gradient(circle, rgba(255,255,255,.75) 0%, rgba(255,190,235,.45) 35%, rgba(255,255,255,.12) 62%, rgba(255,255,255,0) 72%);
    border: 2px solid rgba(255,255,255,.35);
  }

  .services { position: absolute; list-style: none; color: var(--white); font-weight: 500;
    font-size: 17px; line-height: 27px; letter-spacing: .2px; text-transform: uppercase; }
  .services li { display: flex; align-items: center; gap: 10px; }
  .services svg { width: 18px; height: 16px; flex: none; }

  .brand { position: absolute; color: var(--name-grey); font-weight: 500; text-transform: uppercase; line-height: 1; }
  .brand__main { display: block; font-size: 70px; letter-spacing: 1px; }
  .brand__sub { display: block; font-size: 30px; margin-top: 8px; letter-spacing: .5px; }

  .contact { position: absolute; color: var(--name-grey); font-weight: 500; text-transform: uppercase; line-height: 1; }
  .contact__phone { display: block; font-size: 50px; word-spacing: 14px; }
  .contact__web { display: block; font-size: 27px; margin-top: 12px; }

  .heritage { position: absolute; color: var(--ink); text-align: center; text-transform: uppercase; font-weight: 500; line-height: 1.2; }
  .heritage__line { display: block; font-size: 19px; }
  .heritage__year { display: block; font-size: 34px; margin-top: 4px; }
</style>
</head>
<body>

<!-- Driver side: cab at left -->
<section class="wrap-side wrap-side--driver" aria-label="Driver side wrap layout">
  <svg class="art" viewBox="0 0 1100 430" preserveAspectRatio="none" aria-hidden="true">
    <defs>
      <linearGradient id="wash-a" x1="0" y1="0" x2="0" y2="1">
        <stop offset="0" stop-color="#f04aa0"/>
        <stop offset=".4" stop-color="#b331c0"/>
        <stop offset=".7" stop-color="#6a34d6"/>
        <stop offset="1" stop-color="#1f2fb6"/>
      </linearGradient>
    </defs>
    <path d="M600,0 H634 C628,150 560,320 322,430 H300 C520,320 590,160 600,0 Z" fill="var(--ribbon-red)"/>
    <path d="M656,0 H1100 V430 H372 C560,340 650,180 656,0 Z" fill="url(#wash-a)"/>
    <path d="M340,430 C540,330 630,190 640,40" fill="none" stroke="var(--purple)" stroke-width="3"/>
  </svg>

  <div class="glow" role="img" aria-label="Soft sparkle glow decoration" style="left:840px;top:110px;"></div>

  <ul class="services" style="left:780px;top:14px;">
    <li><svg viewBox="0 0 18 16"><path d="M1 9l5 5L17 1" fill="none" stroke="#fff" stroke-width="3"/></svg>Carpet cleaning &amp; maintenance</li>
    <li><svg viewBox="0 0 18 16"><path d="M1 9l5 5L17 1" fill="none" stroke="#fff" stroke-width="3"/></svg>Services, hard surface cleaning</li>
    <li><svg viewBox="0 0 18 16"><path d="M1 9l5 5L17 1" fill="none" stroke="#fff" stroke-width="3"/></svg>Services, water restoration</li>
    <li><svg viewBox="0 0 18 16"><path d="M1 9l5 5L17 1" fill="none" stroke="#fff" stroke-width="3"/></svg>Services &amp; upholstery cleaning</li>
  </ul>

  <div class="brand" style="left:700px;top:150px;">
    <span class="brand__main">Marlowe</span>
    <span class="brand__sub">Carpet Care, Inc.</span>
  </div>

  <div class="contact" style="left:520px;top:270px;">
    <span class="contact__phone">Call 614 555-0142</span>
    <span class="contact__web">www.marlowecarpetcare-example.com.</span>
  </div>

  <div class="heritage" style="left:200px;top:175px;width:260px;">
    <span class="heritage__line">Services to properties</span>
    <span class="heritage__line">throughout Central Ohio</span>
    <span class="heritage__year">Since 1974</span>
  </div>
</section>

<!-- Passenger side: cab at right -->
<section class="wrap-side wrap-side--passenger" aria-label="Passenger side wrap layout">
  <svg class="art" viewBox="0 0 1100 430" preserveAspectRatio="none" aria-hidden="true">
    <defs>
      <linearGradient id="wash-b" x1="0" y1="0" x2="0" y2="1">
        <stop offset="0" stop-color="#f04aa0"/>
        <stop offset=".4" stop-color="#b331c0"/>
        <stop offset=".7" stop-color="#6a34d6"/>
        <stop offset="1" stop-color="#1f2fb6"/>
      </linearGradient>
    </defs>
    <g transform="translate(1100,0) scale(-1,1)">
      <path d="M420,0 H454 C448,150 380,320 142,430 H120 C340,320 410,160 420,0 Z" fill="var(--ribbon-red)"/>
      <path d="M476,0 H1100 V430 H192 C380,340 470,180 476,0 Z" fill="url(#wash-b)"/>
      <path d="M160,430 C360,330 450,190 460,40" fill="none" stroke="var(--purple)" stroke-width="3"/>
    </g>
  </svg>

  <div class="glow" role="img" aria-label="Soft sparkle glow decoration" style="left:0px;top:120px;"></div>

  <ul class="services" style="left:70px;top:14px;">
    <li><svg viewBox="0 0 18 16"><path d="M1 9l5 5L17 1" fill="none" stroke="#fff" stroke-width="3"/></svg>Carpet cleaning &amp; maintenance</li>
    <li><svg viewBox="0 0 18 16"><path d="M1 9l5 5L17 1" fill="none" stroke="#fff" stroke-width="3"/></svg>Services, hard surface cleaning</li>
    <li><svg viewBox="0 0 18 16"><path d="M1 9l5 5L17 1" fill="none" stroke="#fff" stroke-width="3"/></svg>Services, water restoration</li>
    <li><svg viewBox="0 0 18 16"><path d="M1 9l5 5L17 1" fill="none" stroke="#fff" stroke-width="3"/></svg>Services &amp; upholstery cleaning</li>
  </ul>

  <div class="brand" style="left:300px;top:160px;">
    <span class="brand__main">Marlowe</span>
    <span class="brand__sub">Carpet Care, Inc.</span>
  </div>

  <div class="contact" style="left:330px;top:280px;">
    <span class="contact__phone">Call 614 555-0142</span>
    <span class="contact__web">www.marlowecarpetcare-example.com.</span>
  </div>

  <div class="heritage" style="left:760px;top:185px;width:260px;">
    <span class="heritage__line">Services to properties</span>
    <span class="heritage__line">throughout Central Ohio</span>
    <span class="heritage__year">Since 1974</span>
  </div>
</section>

</body>
</html>
```